Tender / Request for Quotation response template

VELKOR42 is a small consulting company that works in management consulting with a particular emphasis on tourism, sport, major events and general commercial. our clients range from government , councils, private businesses and industry associations.

we are regularly asked to submit detailed quotes or tender responses and we use our own PowerPoint template to do so as we find it its generally easier to work with.

our website provides more detail : www.velkor42.com.au the colour of the blue in logo is #000033

our submissions range from 30 pages to 100 pages depending on the size and scale of the project - so we need flexibility with the templates.

Our submissions generally include cover page and table of contents and then
1. Project overview
2. About VELKOR42
3. The project team including bios
4. Initial Insights
5. importance of sustainability
6. Project methodology - example being
6.1 situation analysis
- research
- consultation and engagement
- relevant audits
- relevant economic analysis including graphs
- gap analysis
- SWOT
6.2 Issues and opportunities
6.3 draft report
6.4 final report
7. Case studies and previous relevant work
8. Project timeline
9. Project budget
10. Insurance and referees

we use many graphs and tables from excel and images generally sourced from the web. we also use icons as appropriate so we need graph templates - column, bar / pie etc and table templates.

the feel is on the formal corporate side given the size and scale of projects and clients but with bright and clear graphics and photos.

i have attached 2 copies of confidential submissions that we have made in recent weeks. one long form and one short form to give you an idea of the flexibility we need in the submission process.

if we are happy with the proposed PowerPoint tender submission template we would then look to have a similar one created to use in the development of the actual reports themselves .

hopefully this provides enough information but if not please reach out for more information

our logo and general format are in the attached examples

Target Market(s)

government, council, corporates and private businesses

Industry/Entity Type

management consulting with emphasis on tourism sport major events nd general commerical

Font styles to use
Other font styles liked:
• we usually use calbiri but open to other standard microsoft off the shelf fonts

Colors
0054AA
0677BA
7BADD7
CADEEF
E8F1F8
0094D4
00A9DD
6FCCEA
C7EBF8
E9F6FB

Requirements
Must have
• page for each of the sections detailed in the project brief. image placement - small and large, table and graph formats,

```html
<!DOCTYPE html>
<html lang="en">
<head>
<meta charset="utf-8">
<title>Methodology – A Situational Analysis</title>
<link href="https://fonts.googleapis.com/css2?family=Carlito:ital,wght@0,400;0,700;1,400&family=Roboto+Condensed:wght@700&display=swap" rel="stylesheet">
<style>
  :root{
    --navy:#000033;
    --blue-deep:#0054AA;
    --blue-mid:#0677BA;
    --blue-soft:#7BADD7;
    --cyan:#00A9DD;
    --sky:#6FCCEA;
    --card:#E9F6FB;
    --white:#ffffff;
  }
  *{box-sizing:border-box;margin:0;padding:0}
  html,body{width:1200px;height:675px;overflow:hidden}
  body{font-family:"Carlito",Calibri,sans-serif}
  .slide{
    position:relative;width:1200px;height:675px;overflow:hidden;
    background:radial-gradient(ellipse 900px 300px at 750px 640px,#0a62b8 0%,rgba(10,98,184,0) 70%),
               linear-gradient(180deg,#0054AA 0%,#0050a6 60%,#0058b0 100%);
  }
  .slide-title{
    position:absolute;left:58px;top:16px;
    font-family:"Roboto Condensed",sans-serif;font-weight:700;
    font-size:35px;letter-spacing:-1.2px;color:var(--white);
  }
  .step{
    position:absolute;top:142px;width:246px;height:412px;
    background:var(--card);
    box-shadow:4px 5px 8px rgba(0,20,60,.45);
  }
  .step:nth-of-type(1){left:58px}
  .step:nth-of-type(2){left:329px}
  .step:nth-of-type(3){left:601px}
  .step:nth-of-type(4){left:872px}
  .step-badge{
    position:absolute;left:50%;top:-40px;transform:translateX(-50%);
    width:86px;height:86px;border-radius:50%;background:var(--card);
    display:flex;align-items:center;justify-content:center;
  }
  .step-badge span{
    width:74px;height:74px;border-radius:50%;
    display:flex;align-items:center;justify-content:center;
    font-family:"Roboto Condensed",sans-serif;font-weight:700;font-size:44px;color:var(--white);
  }
  .step-title{
    position:absolute;top:42px;left:0;right:0;text-align:center;
    font-size:20px;line-height:22px;letter-spacing:-.6px;text-transform:uppercase;
  }
  .step-sub{display:block;font-style:italic;font-size:12px;line-height:16px;letter-spacing:-.2px;margin-top:2px}
  .intro{
    position:absolute;top:103px;left:14px;right:14px;text-align:center;
    font-size:10.5px;line-height:13.5px;color:var(--blue-deep);
  }
  .intro p+p{margin-top:13px}
  .tasks{position:absolute;top:103px;left:5px;right:6px;list-style:none;color:var(--blue-deep);font-size:10.5px;line-height:13.5px}
  .tasks li{position:relative;padding-left:16px;margin-bottom:3.5px}
  .tasks li::before{
    content:"";position:absolute;left:1px;top:3px;
    border-left:7px solid var(--blue-deep);border-top:4px solid transparent;border-bottom:4px solid transparent;
  }
  .tasks .note{padding-left:16px;font-style:italic;font-size:9.2px;line-height:12px}
  .tasks .note::before{display:none}
  .s1 .step-badge span{background:var(--cyan)} .s1 .step-title{color:var(--cyan)}
  .s2 .step-badge span{background:var(--blue-mid)} .s2 .step-title{color:var(--blue-deep)}
  .s3 .step-badge span{background:var(--blue-soft)} .s3 .step-title{color:var(--blue-soft)}
  .s4 .step-badge span{background:var(--sky)} .s4 .step-title{color:var(--sky)}
  .s3 .tasks li{margin-bottom:4.2px}
  .brand{position:absolute;left:924px;top:566px;display:flex;align-items:center;gap:6px}
  .brand-mark{width:96px;height:96px;border-radius:50%;background:var(--navy);border:3px solid var(--white)}
  .brand-name{font-family:"Carlito",sans-serif;font-weight:700;font-size:34px;color:var(--white);letter-spacing:.5px}
</style>
</head>
<body>
<main class="slide">
  <h1 class="slide-title">METHODOLOGY - A SITUATIONAL ANALYSIS</h1>

  <section class="step s1">
    <div class="step-badge"><span>1</span></div>
    <h2 class="step-title">Project<br>Inception</h2>
    <div class="intro">
      <p>To initiate a project like this, the initial step is to promptly convene the Project Control Group and hold a thorough Project Inception meeting.</p>
      <p>This meeting will entail a comprehensive conversation covering all vital project aspects, ensuring that every member of the PCG and VELKOR42 shares a consistent understanding of the project's Who, What, Where, When, Why, and How.</p>
    </div>
  </section>

  <section class="step s2">
    <div class="step-badge"><span>2</span></div>
    <h2 class="step-title">Desktop Review<br>and Analysis</h2>
    <ul class="tasks">
      <li>Review HCT Vision documentation</li>
      <li>Review Significance Assessment of the Costume Collection</li>
      <li>Review Preservation Needs Assessment and current collection usage</li>
      <li>Conduct case studies for collection management and display</li>
      <li>Map partners, including major donors and supporters</li>
      <li>Examine property reports for rental and storage options</li>
      <li>Analyze tourism demand</li>
      <li>Apply sustainability principles</li>
      <li>Align strategically with government or private sector plans</li>
      <li class="note">(e.g., Experience Southland Masterplan for 2033, Destination Management Plans, Creative Southland, etc.)</li>
    </ul>
  </section>

  <section class="step s3">
    <div class="step-badge"><span>3</span></div>
    <h2 class="step-title">Stakeholder<br>Engagement</h2>
    <ul class="tasks">
      <li>HCT collection experts and other key staff</li>
      <li>Museum and collection managers</li>
      <li>University fashion course contacts</li>
      <li>Visit Southland</li>
      <li>Harbour City Council and Eastbank Council</li>
      <li>Northvale and Bayport Gallery</li>
      <li>Possible CBD venue owners and property experts</li>
      <li>Tourism Nationwide</li>
      <li>Issues Workshop with HCT Staff</li>
    </ul>
  </section>

  <section class="step s4">
    <div class="step-badge"><span>4</span></div>
    <h2 class="step-title">Site Visits<span class="step-sub">UPTO 8 SITE VISITS</span></h2>
    <ul class="tasks">
      <li>HCT Costume Collection locations</li>
      <li>Potential HCT sites in Melbourne</li>
      <li>University locations</li>
      <li>Other Melbourne CBD or nearby locations (2 or 3)</li>
    </ul>
  </section>

  <div class="brand">
    <div class="brand-mark"></div>
    <span class="brand-name">VELKOR42</span>
  </div>
</main>
</body>
</html>
```